Kivo4 Website design (Need help to re-design our website)

We need someone to help us re-design our website and launch it. All contents for the website are ready. (Website: https://www.kivo4.com.au/)

-Rearrange categories:
1. Heat Pumps (Link to PALOX site: https://palox.com.au/)
2. Solar (Under the Solar category; remove solar panels, solar inverters, and solar batteries)
3. LED
4. Capability Statement
5. Service and Support
6. Contact us

Home page - redesign but the free quote will stay.

NOTE:
-Try using professional fonts (Example: Helvetica, etc.)
-Try to play with colours related to sustainability, eco-friendliness, solar, energy, and energy efficiency.
-The website's Footer should be readable and use light colour.

Target Market(s)

Residentials & commercial buildings

Industry/Entity Type

SOLAR ENERGY PROVIDER

Coding

Coded - Design and coding required

Colors

Designer to choose colors to be used in the design.

Requirements
Nice to have
• Effects/transition on the words/copy/images.

```html
<!DOCTYPE html>
<html lang="en">
<head>
<meta charset="utf-8">
<title>Kivo4 – Solar, Heat Pumps &amp; LED</title>
<link href="https://fonts.googleapis.com/css2?family=Montserrat:wght@500;600;700;800&family=Open+Sans:wght@400;600;700&display=swap" rel="stylesheet">
<style>
:root{
  --blue:#1d5fc4;
  --blue-dark:#0f3f8f;
  --blue-light:#2f8ae0;
  --green:#3ea83a;
  --green-dark:#2b8a2c;
  --ink:#1c2230;
  --muted:#5b6372;
  --line:#e3e7ee;
  --white:#ffffff;
  --star:#f6b400;
  --footer:#f5f7fa;
}
*{box-sizing:border-box;margin:0;padding:0}
html,body{width:1200px;height:3792px;overflow:hidden}
body{font-family:"Open Sans",Arial,sans-serif;color:var(--ink);background:var(--white);position:relative}
h1,h2,h3,h4,.btn,.brand{font-family:"Montserrat",Arial,sans-serif}
.abs{position:absolute}
.brand{display:flex;align-items:center;gap:10px;font-weight:800;font-size:34px;color:var(--blue)}
.brand-dot{width:26px;height:26px;border-radius:50%;background:var(--green)}
.btn{display:inline-block;background:var(--green);color:var(--white);font-weight:700;font-size:13px;letter-spacing:.5px;padding:12px 26px;border-radius:4px;text-transform:uppercase}
.social{display:flex;gap:10px}
.social span{width:34px;height:34px;border-radius:50%;border:2px solid var(--ink);display:block}
.section-title{text-align:center;font-size:34px;font-weight:800;text-transform:uppercase}

/* header */
.topbar{top:0;left:0;width:1200px;height:104px;background:var(--white)}
.topbar .brand{position:absolute;left:128px;top:30px}
.topbar .social{position:absolute;left:700px;top:35px}
.call{position:absolute;left:900px;top:30px;display:flex;gap:12px;align-items:center}
.call-icon{width:44px;height:44px;border-radius:50%;background:var(--blue);display:flex;align-items:center;justify-content:center}
.call small{display:block;font-size:12px;color:var(--muted)}
.call strong{font-family:"Montserrat",sans-serif;font-size:20px;color:var(--blue)}
.nav{top:104px;left:0;width:1200px;height:32px;background:var(--blue);display:flex;align-items:center}
.nav ul{list-style:none;display:flex;gap:26px;margin-left:142px}
.nav li{color:var(--white);font-size:13px;font-weight:600}
.nav .nav-cta{margin-left:auto;width:416px;height:32px;background:var(--green);color:var(--white);font-family:"Montserrat",sans-serif;font-weight:700;font-size:13px;display:flex;align-items:center;justify-content:center}

/* hero */
.hero{top:136px;left:0;width:1200px;height:592px}
.hero-photo{position:absolute;inset:0;background:linear-gradient(180deg,#5b9be0 0%,#9cc6ee 32%,#d8e6ee 44%,#3b5a7a 58%,#1f3450 80%,#4f6b3a 100%)}
.hero-copy{position:absolute;left:142px;top:80px;width:420px;color:var(--white)}
.hero-copy h1{font-size:50px;font-weight:800;margin-bottom:14px}
.hero-copy p{font-size:15px;line-height:1.55;margin-bottom:28px}
.pause{position:absolute;left:142px;top:500px;display:flex;gap:12px;align-items:center;color:var(--white);font-family:"Montserrat",sans-serif;font-weight:700;font-size:15px}
.pause i{width:44px;height:44px;border:2px solid var(--white);border-radius:50%;display:flex;align-items:center;justify-content:center}
.quote-panel{position:absolute;left:784px;top:0;width:416px;height:592px;background:rgba(29,95,196,.92);padding:30px 36px;color:var(--white)}
.quote-panel h2{font-size:28px;font-weight:800;margin-bottom:22px}
.field{height:38px;background:var(--white);border-radius:3px;margin-bottom:10px;display:flex;align-items:center;gap:10px;padding:0 12px;color:#8a93a2;font-size:13px}
.field b{width:12px;height:12px;border-radius:50%;background:var(--blue);display:block}
.quote-panel h4{font-size:13px;font-weight:700;margin:14px 0 8px}
.checks{display:grid;grid-template-columns:1fr 1fr;gap:7px 10px;font-size:12px}
.checks.three{grid-template-columns:1fr 1fr 1fr}
.checks span{display:flex;align-items:center;gap:7px}
.checks span::before{content:"";width:12px;height:12px;background:var(--white);border-radius:2px;flex:none}
.quote-panel .btn{margin-top:22px}

/* services */
.services{top:728px;left:0;width:1200px;height:632px;background:var(--white)}
.services .section-title{margin-top:88px}
.service-card{position:absolute;top:172px;width:288px;height:372px;background:var(--white);border-radius:14px;box-shadow:0 8px 24px rgba(20,40,80,.14);overflow:hidden;text-align:center}
.service-card .media{height:140px}
.service-card h3{font-size:17px;font-weight:700;margin:40px 0 10px}
.service-card p{font-size:12px;line-height:1.6;color:var(--muted);padding:0 26px;margin-bottom:18px}
.service-card .btn{font-size:11px;padding:9px 20px}
.service-card.featured{top:156px;border-bottom:10px solid var(--green)}
.service-card.featured .btn{background:var(--blue)}

/* about */
.about{top:1372px;left:0;width:1200px;height:520px;background:linear-gradient(120deg,var(--blue-light) 0%,var(--blue) 50%,var(--blue-dark) 100%)}
.about-copy{position:absolute;left:142px;top:118px;width:420px;color:var(--white)}
.about-copy h2{font-size:34px;font-weight:800;margin-bottom:16px}
.about-copy p{font-size:13px;line-height:1.6;margin-bottom:14px}
.about-art{position:absolute;left:640px;top:40px;width:420px;height:440px;border-radius:12px;background:linear-gradient(180deg,rgba(255,255,255,.3),rgba(16,40,90,.55))}

/* projects */
.projects{top:1892px;left:0;width:1200px;height:600px}
.projects .section-title{margin-top:124px}
.project{position:absolute;top:188px;width:288px;text-align:center}
.project .media{height:340px;border-radius:12px}
.project p{font-family:"Montserrat",sans-serif;font-weight:700;font-size:15px;margin-top:14px}

/* testimonials */
.testimonials{top:2492px;left:0;width:1200px;height:668px}
.testimonials .bg{position:absolute;inset:0;background:linear-gradient(180deg,#ffffff 0%,#dbeaf7 30%,#6fa3d6 55%,#2e4f78 80%,#4e7a3a 100%)}
.testimonials .section-title{position:relative;padding-top:84px}
.review{position:absolute;top:172px;width:288px;height:200px;background:var(--white);border-radius:12px;box-shadow:0 8px 24px rgba(20,40,80,.16);padding:22px 24px}
.stars{display:flex;gap:3px;margin-bottom:10px}
.review p{font-size:11.5px;line-height:1.55;color:var(--muted);margin-bottom:14px}
.who{display:flex;gap:10px;align-items:center}
.avatar{width:36px;height:36px;border-radius:50%;background:#c9d3df}
.who strong{display:block;font-size:13px}
.who small{font-size:11px;color:var(--muted)}

/* accreditations */
.partners{top:3160px;left:0;width:1200px;height:288px;background:linear-gradient(180deg,var(--green) 0%,var(--green-dark) 100%)}
.partners .section-title{color:var(--white);margin-top:44px}
.badge{position:absolute;top:164px;width:150px;height:84px;background:var(--white);border-radius:10px}
.badge i{position:absolute;left:30px;top:24px;width:90px;height:36px;border-radius:6px;background:#e4e8ee;display:block}
.arrow{position:absolute;top:192px;width:30px;height:30px;border-radius:50%;background:var(--white);display:flex;align-items:center;justify-content:center}

/* footer */
.footer{top:3448px;left:0;width:1200px;height:344px;background:var(--footer)}
.footer .brand{position:absolute;left:190px;top:56px}
.footer .social{position:absolute;left:200px;top:130px}
.footer-col{position:absolute;top:52px}
.footer-col h4{font-size:14px;font-weight:700;margin-bottom:16px;padding-left:14px;border-left:3px solid var(--green)}
.footer-col ul{list-style:none;font-size:13px;color:var(--muted);line-height:2}
.contact li{display:flex;gap:10px;align-items:flex-start;margin-bottom:10px;line-height:1.5}
.contact b{width:14px;height:14px;border-radius:50%;background:var(--green);flex:none;margin-top:3px}
.legal{position:absolute;left:0;top:300px;width:1200px;height:44px;border-top:1px solid var(--line);display:flex;align-items:center;justify-content:space-between;padding:0 140px;font-size:12px;color:var(--muted)}
</style>
</head>
<body>

<header class="abs topbar">
  <div class="brand"><span class="brand-dot"></span>Kivo4</div>
  <div class="social" aria-label="Social links"><span></span><span></span><span></span></div>
  <div class="call">
    <div class="call-icon"><svg width="20" height="20" viewBox="0 0 24 24"><path d="M6.6 10.8a15 15 0 0 0 6.6 6.6l2.2-2.2a1 1 0 0 1 1-.25 11.4 11.4 0 0 0 3.6.6 1 1 0 0 1 1 1V20a1 1 0 0 1-1 1A17 17 0 0 1 3 4a1 1 0 0 1 1-1h3.5a1 1 0 0 1 1 1c0 1.25.2 2.45.6 3.6a1 1 0 0 1-.25 1z" fill="#fff"/></svg></div>
    <div><small>Call Us Today</small><strong>1300 555 014</strong></div>
  </div>
</header>

<nav class="abs nav">
  <ul><li>Heat Pumps</li><li>Solar</li><li>LED</li><li>Capability Statement</li><li>Service and Support</li><li>Contact us</li></ul>
  <div class="nav-cta">GET A FREE QUOTE</div>
</nav>

<section class="abs hero">
  <div class="hero-photo" role="img" aria-label="Rows of solar panels on a field under a blue sky"></div>
  <div class="hero-copy">
    <h1>Kivo4</h1>
    <p>Power bills have risen dramatically in Australia over the past decade, making energy bills amongst the highest household costs.</p>
    <span class="btn">Get a free quote</span>
  </div>
  <div class="pause"><i><svg width="14" height="16" viewBox="0 0 14 16"><rect x="1" y="0" width="4" height="16" fill="#fff"/><rect x="9" y="0" width="4" height="16" fill="#fff"/></svg></i>PAUSE</div>
  <form class="quote-panel">
    <h2>GET STARTED TODAY</h2>
    <div class="field"><b></b>Full Name</div>
    <div class="field"><b></b>Email Address</div>
    <div class="field"><b></b>Phone</div>
    <div class="field"><b></b>Address</div>
    <h4>I am interested in</h4>
    <div class="checks"><span>Solar For Homes</span><span>Solar For Business</span><span>Heat Pump For Homes</span><span>Heat Pump For Business</span></div>
    <h4>I heard about you from</h4>
    <div class="checks three"><span>Social</span><span>Search</span><span>Referral</span><span>Video</span><span>Other</span></div>
    <span class="btn">Submit now</span>
  </form>
</section>

<section class="abs services">
  <h2 class="section-title">Our Services</h2>
  <article class="service-card" style="left:144px">
    <div class="media" role="img" aria-label="Heat pump unit installed outside a home" style="background:linear-gradient(135deg,#e8d8c4,#b9a38a)"></div>
    <h3>HEAT PUMPS</h3>
    <p>Deliver home comfort with our efficient water heaters, ensuring both comfort and substantial electric bill savings.</p>
    <span class="btn">Learn more</span>
  </article>
  <article class="service-card featured" style="left:456px">
    <div class="media" role="img" aria-label="Bright LED lighting in a commercial space" style="background:linear-gradient(135deg,#eef3f6,#9fb6c4)"></div>
    <h3>LED</h3>
    <p>For commercial businesses keeping operating costs low is crucial. Typically we cut lighting expenses.</p>
    <span class="btn">Learn more</span>
  </article>
  <article class="service-card" style="left:768px">
    <div class="media" role="img" aria-label="Solar panels on a roof" style="background:linear-gradient(135deg,#7fb0dc,#254a74)"></div>
    <h3>SOLAR</h3>
    <p>Elevate home comfort with our efficient solar systems, ensuring both comfort and substantial electric bill savings.</p>
    <span class="btn">Learn more</span>
  </article>
</section>

<section class="abs about">
  <div class="about-copy">
    <h2>ABOUT KIVO4</h2>
    <p>Power bills have risen dramatically in Australia over the past decade making energy bills amongst the highest utility expenses for businesses and households alike.</p>
    <p><strong>That's where we come in!</strong></p>
    <p>We are a completely Australian Owned and Operated company that specialise in adopting the latest technologies to improve your energy efficiency and reduce costs.</p>
    <span class="btn">Learn more</span>
  </div>
  <div class="about-art" role="img" aria-label="Illustration of angled solar panel rows"></div>
</section>

<section class="abs projects">
  <h2 class="section-title">Our Recent Projects</h2>
  <div class="project" style="left:144px"><div class="media" role="img" aria-label="Commercial roof with solar installation" style="background:linear-gradient(180deg,#8dbbe6,#9a9a94)"></div><p>250 kW</p></div>
  <div class="project" style="left:456px"><div class="media" role="img" aria-label="Warehouse roof covered with solar panels" style="background:linear-gradient(180deg,#a9c9e6,#55677a)"></div><p>100 kW</p></div>
  <div class="project" style="left:768px"><div class="media" role="img" aria-label="Solar array on a flat roof" style="background:linear-gradient(180deg,#6fa6dc,#23456e)"></div><p>99 kW</p></div>
  <div class="project" style="left:1080px"><div class="media" role="img" aria-label="Solar panels on a factory roof" style="background:linear-gradient(180deg,#b7d1e8,#a05a3c)"></div><p>30 kW</p></div>
</section>

<section class="abs testimonials">
  <div class="bg" role="img" aria-label="Solar panel field under the sky"></div>
  <h2 class="section-title">What Our Client Says</h2>
  <article class="review" style="left:144px">
    <div class="stars"><svg width="90" height="16" viewBox="0 0 90 16"><g fill="#f6b400"><path id="s" d="M8 0l2.4 5 5.6.6-4.2 3.8 1.2 5.6L8 12.2 3 15l1.2-5.6L0 5.6 5.6 5z"/><use href="#s" x="18"/><use href="#s" x="36"/><use href="#s" x="54"/><use href="#s" x="72"/></g></svg></div>
    <p>Kivo4 are an awesome company with high levels of professionalism. Our panels were installed promptly with no issues. The team goes above and beyond.</p>
    <div class="who"><span class="avatar"></span><div><strong>Marla Chesney</strong><small>VIC</small></div></div>
  </article>
  <article class="review" style="left:456px">
    <div class="stars"><svg width="90" height="16" viewBox="0 0 90 16"><g fill="#f6b400"><use href="#s"/><use href="#s" x="18"/><use href="#s" x="36"/><use href="#s" x="54"/><use href="#s" x="72"/></g></svg></div>
    <p>I am very happy with Kivo4 solar install at my place. Their rates were the most competitive when I shopped around. Fast advice and great result.</p>
    <div class="who"><span class="avatar"></span><div><strong>Rohan Devar</strong><small>VIC</small></div></div>
  </article>
  <article class="review" style="left:768px">
    <div class="stars"><svg width="90" height="16" viewBox="0 0 90 16"><g fill="#f6b400"><use href="#s"/><use href="#s" x="18"/><use href="#s" x="36"/><use href="#s" x="54"/><use href="#s" x="72"/></g></svg></div>
    <p>I have been dealing with this company for the past 5 years and have found they are very prompt, engaging with customers and contractors, very transparent.</p>
    <div class="who"><span class="avatar"></span><div><strong>Owen T</strong><small>VIC</small></div></div>
  </article>
</section>

<section class="abs partners">
  <h2 class="section-title">Accreditations &amp; Partners</h2>
  <span class="arrow" style="left:84px"><svg width="10" height="12" viewBox="0 0 10 12"><path d="M8 0L0 6l8 6z" fill="#1c2230"/></svg></span>
  <div class="badge" style="left:144px"><i></i></div>
  <div class="badge" style="left:328px"><i></i></div>
  <div class="badge" style="left:512px"><i></i></div>
  <div class="badge" style="left:696px"><i></i></div>
  <div class="badge" style="left:880px"><i></i></div>
  <span class="arrow" style="left:1086px"><svg width="10" height="12" viewBox="0 0 10 12"><path d="M2 0l8 6-8 6z" fill="#1c2230"/></svg></span>
</section>

<footer class="abs footer">
  <div class="brand"><span class="brand-dot"></span>Kivo4</div>
  <div class="social" aria-label="Social links"><span></span><span></span><span></span></div>
  <div class="footer-col" style="left:460px">
    <h4>QUICK LINKS</h4>
    <ul><li>Heat Pumps</li><li>Solar</li><li>LED</li><li>Capability Statement</li><li>Service and Support</li><li>Contact Us</li></ul>
  </div>
  <div class="footer-col contact" style="left:800px">
    <h4>CONTACT INFO</h4>
    <ul>
      <li><b></b>12 Wattle Lane Northvale<br>VIC 3000</li>
      <li><b></b>enquiries@kivo4.com.au</li>
      <li><b></b>1300 555 014</li>
    </ul>
  </div>
  <div class="legal"><span>© 2024 Kivo4 - All Rights Reserved</span><span>Privacy &nbsp;|&nbsp; Terms &nbsp;|&nbsp; Disclaimer</span></div>
</footer>

</body>
</html>
```